Industrial Laundry News Paper Add

We need a color add for 1/4 page newspaper using blue and white. We are an industrial laundry providing linen washing for condo rental companies. We can provide linen rental and wash customer-owned goods

```html
<!DOCTYPE html>
<html lang="en">
<head>
<meta charset="utf-8">
<title>Summit Ridge Services – Industrial Laundry</title>
<link href="https://fonts.googleapis.com/css2?family=Bebas+Neue&family=Open+Sans:wght@400;600;700;800&family=Source+Sans+3:wght@700;800&display=swap" rel="stylesheet">
<style>
  :root {
    --navy: #27307a;
    --royal: #274a8f;
    --slate: #7388b9;
    --pill: #5873a8;
    --grey-type: #666666;
    --ink: #222222;
    --white: #ffffff;
    --frame: #9a9a9a;
  }
  * { margin: 0; padding: 0; box-sizing: border-box; }
  html, body { width: 847px; height: 1200px; overflow: hidden; background: var(--white); }
  body { position: relative; font-family: "Open Sans", sans-serif; color: var(--ink); }

  .ad { position: absolute; left: 83px; top: 68px; width: 687px; height: 1054px; border: 1px solid var(--frame); overflow: hidden; background: var(--white); }
  .layer { position: absolute; left: 0; top: 0; }

  .brand { position: absolute; left: 40px; top: 108px; width: 305px; text-align: center; }
  .brand__name { display: flex; align-items: center; justify-content: center; gap: 10px; font-family: "Open Sans", sans-serif; font-weight: 800; font-size: 27px; line-height: 1.05; color: var(--royal); }
  .brand__dot { width: 14px; height: 14px; border-radius: 50%; background: var(--royal); flex: none; }
  .brand__tagline { margin-top: 6px; font-size: 12px; letter-spacing: 0.2px; color: var(--royal); white-space: nowrap; }

  .phone { position: absolute; left: 384px; top: 33px; display: flex; align-items: center; gap: 6px; font-family: "Open Sans", sans-serif; font-weight: 800; font-size: 31px; color: var(--royal); }
  .phone__icon { width: 30px; height: 30px; border-radius: 4px; background: var(--royal); display: flex; align-items: center; justify-content: center; }
  .call-pill { position: absolute; left: 384px; top: 75px; width: 274px; height: 32px; border-radius: 16px; background: var(--pill); color: var(--white); font-weight: 700; font-size: 23px; line-height: 32px; text-align: center; box-shadow: 0 10px 8px -6px rgba(0,0,0,0.45); }

  .headline { position: absolute; left: 30px; top: 484px; font-family: "Source Sans 3", sans-serif; font-weight: 800; color: var(--slate); line-height: 1; white-space: nowrap; }
  .headline__lead { display: block; font-size: 52px; letter-spacing: -1.5px; }
  .headline__main { display: block; margin-top: 4px; margin-left: 8px; font-size: 61px; letter-spacing: -0.5px; }

  .offer { position: absolute; left: 38px; top: 614px; width: 440px; color: var(--royal); }
  .offer__title { font-weight: 800; font-size: 25px; line-height: 24px; letter-spacing: 0.2px; }
  .offer__sub { margin-top: 14px; font-weight: 800; font-size: 17.5px; line-height: 19px; }

  .about { position: absolute; left: 479px; top: 614px; width: 192px; font-size: 15.5px; line-height: 19.2px; color: var(--ink); }

  .service { position: absolute; font-family: "Bebas Neue", sans-serif; color: var(--grey-type); font-size: 29px; line-height: 28px; text-align: center; }
  .service--carpet { left: 50px; top: 742px; width: 130px; }
  .service--laundry { left: 240px; top: 739px; width: 150px; }

  .contact { position: absolute; left: 424px; top: 938px; color: var(--white); font-size: 15px; line-height: 20.5px; font-style: normal; }
  .contact__row { display: flex; gap: 6px; align-items: flex-start; }
  .contact__row svg { margin-top: 4px; flex: none; }
  .contact__row--indent { padding-left: 19px; }
  .web { position: absolute; left: 301px; top: 1012px; display: flex; align-items: center; gap: 8px; color: var(--white); font-weight: 700; font-size: 20px; }
</style>
</head>
<body>
<main class="ad">
  <svg class="layer" width="687" height="1054" viewBox="0 0 687 1054">
    <defs>
      <linearGradient id="washerFade" x1="0" y1="0" x2="0" y2="1">
        <stop offset="0" stop-color="#6f7780"/>
        <stop offset="0.45" stop-color="#a9afb6"/>
        <stop offset="0.85" stop-color="#e7e9ec"/>
        <stop offset="1" stop-color="#ffffff"/>
      </linearGradient>
      <linearGradient id="bandFill" x1="0" y1="0" x2="1" y2="0">
        <stop offset="0" stop-color="#2a4c92"/>
        <stop offset="1" stop-color="#262a6c"/>
      </linearGradient>
      <radialGradient id="linenFill" cx="0.5" cy="0.5" r="0.6">
        <stop offset="0" stop-color="#f7f8fa"/>
        <stop offset="1" stop-color="#d6d9df"/>
      </radialGradient>
      <radialGradient id="carpetFill" cx="0.5" cy="0.5" r="0.6">
        <stop offset="0" stop-color="#cfc5bb"/>
        <stop offset="1" stop-color="#8b8580"/>
      </radialGradient>
      <radialGradient id="workerFill" cx="0.5" cy="0.5" r="0.6">
        <stop offset="0" stop-color="#e6eaee"/>
        <stop offset="1" stop-color="#3c8c9c"/>
      </radialGradient>
    </defs>

    <path role="img" aria-label="Row of stainless industrial washing machines" d="M0 250 C 40 290, 120 300, 220 270 C 360 225, 520 150, 687 160 L 687 470 L 0 470 Z" fill="url(#washerFade)"/>

    <path d="M0 195 C 10 255, 90 275, 180 262 C 330 238, 500 130, 640 132 C 665 133, 680 140, 687 148 L 687 170 C 660 150, 600 150, 520 170 C 400 205, 270 275, 160 277 C 80 279, 20 262, 0 245 Z" fill="var(--navy)"/>
    <path d="M520 145 C 600 118, 660 126, 687 143 L 687 160 C 650 138, 600 135, 520 145 Z" fill="var(--royal)"/>

    <circle cx="553" cy="388" r="121" fill="#ffffff"/>
    <circle role="img" aria-label="Hands folding a stack of white linens" cx="553" cy="388" r="108" fill="url(#linenFill)"/>

    <path d="M0 954 C 80 990, 200 985, 320 940 C 420 905, 540 885, 687 920 L 687 1054 L 0 1054 Z" fill="url(#bandFill)"/>

    <circle cx="116" cy="901" r="91" fill="#ffffff"/>
    <circle role="img" aria-label="Carpet being cleaned with an extraction wand" cx="116" cy="901" r="80" fill="url(#carpetFill)"/>
    <circle cx="315" cy="901" r="91" fill="#ffffff"/>
    <circle role="img" aria-label="Laundry worker folding towels beside a commercial washer" cx="315" cy="901" r="80" fill="url(#workerFill)"/>
  </svg>

  <div class="brand">
    <div class="brand__name"><span class="brand__dot"></span><span>SUMMIT RIDGE<br>SERVICES</span></div>
    <div class="brand__tagline">HOUSKEEPING·LAUNDRY·CARPET CLEANING</div>
  </div>

  <div class="phone">
    <span class="phone__icon">
      <svg width="18" height="18" viewBox="0 0 24 24"><path d="M6.6 10.8a15.1 15.1 0 0 0 6.6 6.6l2.2-2.2c.3-.3.7-.4 1-.2 1.1.4 2.3.6 3.6.6.6 0 1 .4 1 1V20c0 .6-.4 1-1 1A17 17 0 0 1 3 4c0-.6.4-1 1-1h3.5c.6 0 1 .4 1 1 0 1.2.2 2.4.6 3.6.1.3 0 .7-.2 1z" fill="#ffffff"/></svg>
    </span>
    1 555-010-4420
  </div>
  <div class="call-pill">CALL US TODAY !</div>

  <h1 class="headline">
    <span class="headline__lead">THE FIRST NAME IN</span>
    <span class="headline__main">INDUSTRIAL LAUNDRY</span>
  </h1>

  <section class="offer">
    <h2 class="offer__title">PROVIDING LINEN WASHING<br>FOR CONDO RENTAL COMPANIES.</h2>
    <p class="offer__sub">WE CAN PROVIDE LINEN RENTAL AND WASH<br>CUSTOMER-OWNED GOODS</p>
  </section>

  <p class="about">Summit Ridge Services is a family-owned and operated cleaning company. Our goal is to continued growth by offering customers a consistent, reliable total cleaning solution day in and day out. We always strive to combine industry experience with the latest cleaning technologies and environmentally friendly products</p>

  <div class="service service--carpet">CARPET<br>CLEANING</div>
  <div class="service service--laundry">COMMERCIAL<br>LAUNDRY</div>

  <address class="contact">
    <div class="contact__row">
      <svg width="13" height="12" viewBox="0 0 13 12"><rect x="0.5" y="2.5" width="12" height="9" fill="none" stroke="#fff"/><path d="M0.5 2.5 L6.5 7.5 L12.5 2.5" fill="none" stroke="#fff"/></svg>
      <span>info@summitridgeservices.com</span>
    </div>
    <div class="contact__row">
      <svg width="13" height="14" viewBox="0 0 12 16"><path d="M6 0a6 6 0 0 0-6 6c0 4.5 6 10 6 10s6-5.5 6-10a6 6 0 0 0-6-6zm0 8.3A2.3 2.3 0 1 1 6 3.7a2.3 2.3 0 0 1 0 4.6z" fill="#fff"/></svg>
      <span>128 Valley Way, Pine Hollow,</span>
    </div>
    <div class="contact__row contact__row--indent">CA 90000, USA</div>
  </address>

  <div class="web">
    <svg width="22" height="22" viewBox="0 0 22 22"><circle cx="10" cy="10" r="8.5" fill="none" stroke="#fff" stroke-width="1.6"/><ellipse cx="10" cy="10" rx="3.8" ry="8.5" fill="none" stroke="#fff" stroke-width="1.4"/><path d="M1.5 10h17M3 5.5h14M3 14.5h14" stroke="#fff" stroke-width="1.3"/><path d="M13 13l7 3-3 1-1 3z" fill="#fff"/></svg>
    <span>www.summitridgeservices.com</span>
  </div>
</main>
</body>
</html>
```